Criação de Folheto ou Cartaz (sem dobra) para Consultoria de Negócios
" Ajudamos empresa a identificar os seus principais gaps e definir/ executar ações para crescimento em 5 focos (4 Pilares da Ascensão): capacidade de execução, eficiência financeira, estratégia de crescimento, Ciclo de Gente, Governança. www.torvenaquesta.com "

```html
<!DOCTYPE html>
<html lang="pt-BR">
<head>
<meta charset="utf-8">
<title>Torvena Growth Consulting – Cartaz</title>
<link rel="stylesheet" href="https://fonts.googleapis.com/css2?family=Montserrat:wght@400;500;600;700&family=Open+Sans:wght@300;400;600;700&display=swap">
<style>
  :root {
    --navy: #14284a;
    --navy-deep: #0d1c36;
    --gold: #d9b45a;
    --gold-light: #f3dc9a;
    --cream: #fbf3d9;
    --white: #ffffff;
    --ink: #1d2d4d;
    --stage: #eceef0;
  }
  * { margin: 0; padding: 0; box-sizing: border-box; }
  html, body { width: 1200px; height: 1200px; overflow: hidden; }
  body {
    background: var(--stage);
    font-family: "Open Sans", Arial, sans-serif;
    color: var(--ink);
  }
  .poster {
    position: absolute;
    left: 200px; top: 30px;
    width: 800px; height: 1140px;
    background: var(--white);
    overflow: hidden;
    box-shadow: 0 6px 24px rgba(0,0,0,0.18);
  }
  .poster-art { position: absolute; inset: 0; width: 800px; height: 1140px; }

  .brand {
    position: absolute; top: 42px; left: 0; width: 100%;
    display: flex; flex-direction: column; align-items: center;
  }
  .brand-row { display: flex; align-items: center; gap: 14px; }
  .brand-mark { width: 22px; height: 22px; background: var(--gold); }
  .brand-name {
    font-family: "Montserrat", Arial, sans-serif;
    font-weight: 600; font-size: 34px; letter-spacing: 7px;
    color: var(--navy);
  }
  .brand-tagline {
    font-family: "Montserrat", Arial, sans-serif;
    font-size: 11px; letter-spacing: 5px; color: var(--navy);
    margin-top: 4px; margin-left: 36px;
  }

  .headline {
    position: absolute; top: 285px; left: 0; width: 100%;
    text-align: center; color: var(--white);
  }
  .headline-line { font-weight: 300; font-size: 38px; line-height: 46px; }
  .headline-line strong { font-weight: 600; }
  .headline-key { font-weight: 700; font-size: 64px; line-height: 72px; }

  .stats-lead {
    position: absolute; left: 70px; top: 575px; width: 200px;
    font-weight: 600; font-size: 26px; line-height: 31px; color: var(--navy);
  }
  .stat {
    position: absolute; width: 120px; text-align: center;
  }
  .stat-value {
    height: 96px; display: flex; align-items: center; justify-content: center;
    font-weight: 400; font-size: 30px; color: var(--navy);
  }
  .stat-note {
    margin-top: 8px; font-size: 10.5px; line-height: 13px; color: var(--navy);
  }
  .stat-75 { left: 308px; top: 581px; }
  .stat-50 { left: 465px; top: 550px; }
  .stat-25 { left: 605px; top: 521px; }

  .pillars {
    position: absolute; right: 45px; top: 812px; width: 320px;
  }
  .pillars-title {
    font-weight: 400; font-size: 25px; line-height: 32px; color: var(--navy);
    margin-bottom: 32px;
  }
  .pillars-list { list-style: none; text-align: right; }
  .pillars-list li {
    font-size: 18px; line-height: 26px; color: var(--navy);
    display: flex; justify-content: flex-end; align-items: center; gap: 10px;
  }
  .pillars-list li::after {
    content: ""; width: 7px; height: 7px; border-radius: 50%; background: var(--navy);
  }

  .site {
    position: absolute; left: 0; bottom: 24px; width: 100%; text-align: center;
    font-family: "Montserrat", Arial, sans-serif;
    font-weight: 500; font-size: 19px; letter-spacing: 7px; color: var(--gold);
  }
</style>
</head>
<body>
<main class="poster">
  <svg class="poster-art" viewBox="0 0 800 1140" aria-hidden="false">
    <defs>
      <linearGradient id="teamPhotoTone" x1="0" y1="0" x2="1" y2="1">
        <stop offset="0" stop-color="#2b4068"/>
        <stop offset="0.5" stop-color="#1a2d52"/>
        <stop offset="1" stop-color="#0f1f3c"/>
      </linearGradient>
      <linearGradient id="goldBand" x1="0" y1="0" x2="1" y2="0.4">
        <stop offset="0" stop-color="#e7c46e"/>
        <stop offset="0.6" stop-color="#f6e3a7"/>
        <stop offset="1" stop-color="#fbf1d2"/>
      </linearGradient>
      <linearGradient id="bridgePhotoTone" x1="0" y1="0" x2="1" y2="0">
        <stop offset="0" stop-color="#7ea7cf"/>
        <stop offset="0.4" stop-color="#b9d2ea"/>
        <stop offset="0.72" stop-color="#ffffff"/>
      </linearGradient>
    </defs>

    <g role="img" aria-label="Foto de equipe trabalhando em escritório, em tom azul escuro">
      <rect x="0" y="60" width="800" height="470" fill="url(#teamPhotoTone)"/>
    </g>

    <!-- header band -->
    <path d="M0 0 H800 V130 C640 130 480 160 400 220 C320 160 160 130 0 130 Z" fill="var(--navy)"/>
    <path d="M0 0 H800 V112 C640 112 480 140 400 202 C320 140 160 112 0 112 Z" fill="var(--gold)"/>
    <path d="M0 0 H800 V104 C640 104 480 130 400 192 C320 130 160 104 0 104 Z" fill="var(--white)"/>

    <!-- stats band -->
    <path d="M0 440 Q400 600 800 440 V490 Q400 640 0 490 Z" fill="var(--white)"/>
    <path d="M0 470 Q400 620 800 470 V490 Q400 640 0 490 Z" fill="var(--gold)"/>
    <path d="M0 490 Q400 640 800 490 V690 Q400 700 0 745 Z" fill="url(#goldBand)"/>
    <path d="M0 560 L120 620 L0 690 Z" fill="#f8e7b3" opacity="0.6"/>

    <!-- progress rings -->
    <g fill="var(--white)" stroke-width="8">
      <circle cx="368" cy="629" r="46" stroke="#e4e8ef"/>
      <circle cx="368" cy="629" r="46" stroke="var(--navy)" fill="none" stroke-dasharray="217 289" transform="rotate(-90 368 629)"/>
      <circle cx="525" cy="598" r="46" stroke="#e4e8ef"/>
      <circle cx="525" cy="598" r="46" stroke="var(--navy)" fill="none" stroke-dasharray="145 289" transform="rotate(-90 525 598)"/>
      <circle cx="665" cy="569" r="46" stroke="#e4e8ef"/>
      <circle cx="665" cy="569" r="46" stroke="var(--navy)" fill="none" stroke-dasharray="72 289" transform="rotate(-90 665 569)"/>
    </g>

    <g role="img" aria-label="Foto de ponte estaiada sobre rio com céu azul claro">
      <path d="M0 760 Q400 712 800 700 V1056 H0 Z" fill="url(#bridgePhotoTone)"/>
    </g>

    <!-- footer -->
    <rect x="0" y="1050" width="800" height="8" fill="var(--gold)"/>
    <rect x="0" y="1058" width="800" height="82" fill="var(--navy-deep)"/>
  </svg>

  <header class="brand">
    <div class="brand-row">
      <span class="brand-mark"></span>
      <span class="brand-name">TORVENA</span>
    </div>
    <span class="brand-tagline">GROWTH CONSULTING</span>
  </header>

  <h1 class="headline">
    <span class="headline-line" style="display:block">Ajudando empreendedores</span>
    <span class="headline-line" style="display:block">a <strong>superar as dores do</strong></span>
    <span class="headline-key" style="display:block">crescimento</span>
  </h1>

  <p class="stats-lead">A maioria dos negócios não cresce e fecha as portas</p>

  <div class="stat stat-75">
    <div class="stat-value">75%</div>
    <p class="stat-note">Das empresas que fracassam em menos de 10 anos</p>
  </div>
  <div class="stat stat-50">
    <div class="stat-value">50%</div>
    <p class="stat-note">Das empresas que fracassam em menos de 5 anos</p>
  </div>
  <div class="stat stat-25">
    <div class="stat-value">25%</div>
    <p class="stat-note">Das empresas que fracassam em menos de 2 anos</p>
  </div>

  <section class="pillars">
    <h2 class="pillars-title">4 Pilares da Ascensão:</h2>
    <ul class="pillars-list">
      <li>Capacidade de Execução</li>
      <li>Eficiência Financeira</li>
      <li>Estratégia de Crescimento</li>
      <li>DNA e Ciclo de Gente</li>
      <li>Alavancagem da Governança</li>
    </ul>
  </section>

  <footer class="site">www.torvenaquesta.com</footer>
</main>
</body>
</html>
```